Business Card Design Project - bel soravin group

dear Sirs

we need business card design for our group ( BEL Soravin Group ) , i have got the Logo design of our group from pixel harbor in previous , so all need details relating to our group i think available with you, as well as the the chosen logo design

we hope to provide us with business card logo that to be appropaite and satisfactory to us .

thanks

note : logo design of our group is attached .
Updates

Reason: please extend the deadline of my project for additional 15 days because i didn't received appropriate design for our gruop yet . kindly beaware that i have received 77 design till now , supossed to send me 200-250 design at least . thanks

Target Market(s)

contents
-

name : Korvan EL Mistrani

position : Operation Manager

Industry/Entity Type

Business

Requirements
Must have

• person name

group logo
Nice to have
• logo color matching with back background

```html
<!DOCTYPE html>
<html lang="en">
<head>
<meta charset="utf-8">
<title>BEL Soravin Group – Business Card</title>
<link href="https://fonts.googleapis.com/css2?family=Open+Sans:ital,wght@0,400;0,700;1,700&display=swap" rel="stylesheet">
<style>
  :root {
    --stage: #45484b;
    --card: #ffffff;
    --brand-navy: #0d4f93;
    --brand-blue: #1670bf;
    --text-grey: #6e6e6e;
    --band-top: #6aa3dc;
    --band-mid: #1a78c8;
    --band-bottom: #0f63b0;
  }
  * { box-sizing: border-box; margin: 0; padding: 0; }
  html, body {
    width: 1200px; height: 1200px; overflow: hidden;
    background: var(--stage);
    font-family: "Open Sans", sans-serif;
  }
  .card {
    position: absolute;
    top: 443px;
    width: 521px; height: 312px;
    background: var(--card);
    box-shadow: 4px 5px 10px rgba(0,0,0,0.35);
    overflow: hidden;
  }
  .card--front { left: 54px; }
  .card--back { left: 624px; }

  .wordmark {
    position: absolute;
    display: flex; align-items: center;
    color: var(--brand-navy);
    font-weight: 700;
    white-space: nowrap;
    line-height: 1;
  }
  .wordmark__square { display: block; background: var(--brand-navy); flex: none; }
  .card--front .wordmark { left: 40px; top: 55px; font-size: 22px; gap: 8px; }
  .card--front .wordmark__square { width: 18px; height: 18px; }
  .card--back .wordmark { left: 70px; top: 138px; font-size: 40px; gap: 14px; }
  .card--back .wordmark__square { width: 32px; height: 32px; }

  .person { position: absolute; right: 39px; top: 62px; text-align: right; }
  .person__name { color: var(--brand-blue); font-weight: 700; font-size: 16px; line-height: 22px; }
  .person__role { color: var(--text-grey); font-size: 12px; line-height: 16px; }

  .address, .contact {
    position: absolute; font-size: 13px; line-height: 18.75px; color: var(--text-grey);
    font-style: normal; white-space: nowrap;
  }
  .address { left: 39px; top: 219px; }
  .contact { right: 39px; top: 200px; text-align: right; }
  .contact .domain { color: var(--brand-blue); }

  .band {
    position: absolute; left: 0; right: 0; bottom: 0; height: 33px;
    border-top: 2px solid var(--band-mid);
    background: linear-gradient(to bottom, var(--band-top) 0%, var(--band-mid) 45%, var(--band-bottom) 100%);
  }

  .website {
    position: absolute; right: 68px; top: 90px;
    color: var(--brand-blue); font-weight: 700; font-style: italic; font-size: 13px;
  }
  .rule {
    position: absolute; left: 70px; right: 68px; top: 113px;
    height: 4px; background: var(--brand-navy);
  }
</style>
</head>
<body>
  <section class="card card--front" aria-label="Business card front">
    <div class="wordmark"><span class="wordmark__square"></span>BEL Soravin Group</div>
    <div class="person">
      <p class="person__name">Korvan EL Mistrani</p>
      <p class="person__role">Operation Manager</p>
    </div>
    <address class="address">
      dummy dummy&nbsp; dummy<br>
      dummy dummy&nbsp; City&nbsp; dummy<br>
      Country&nbsp; dummy land
    </address>
    <div class="contact">
      (083) 555201<br>
      (083) 5552019<br>
      +63 917 5550148<br>
      korvan@<span class="domain">belsoravingroup</span>.com
    </div>
    <div class="band"></div>
  </section>

  <section class="card card--back" aria-label="Business card back">
    <p class="website">www.belsoravingroup.com</p>
    <div class="rule"></div>
    <div class="wordmark"><span class="wordmark__square"></span>BEL Soravin Group</div>
  </section>
</body>
</html>
```